Liquor Label / Aguardiente

Label design for liquor bottle. Designers may submit multiple submissions.

Product Description:
Name: Luna de Cobre™
Alcohol Category: Aguardiente (which in Spanish most closely translates to “burning water”) – aguardiente is derived from
cane sugar and is a general term for a type of alcoholic spirit in many Central and South America countries.
Taste: A smooth liquor with a comfortable yet spicy finish
Smell: Subtle aroma of spicy jalapeños
Liquid Color: Clear
Bottle Color: Clear
See link for reference - http://www.pellowinery.example/sites/default/files/styles/uc_product_full/public/Vessel_0.jpg?itok=8KqTm2Xw
Closure: Bar top / cork
Bottle Shape/Size: height = 8.67in; diameter of base = 3.70in; diameter of neck = 0.85in

Label may consist of two separate parts (i.e. front and back, front and vertical side), or one continuous label.

Designer has complete freedom with color, font etc. unless otherwise stated below. The label MUST
contain (but is not limited only to) the following text exactly as written in quotes below:
- “Luna de Cobre”
- “Aguardiente”
- “Cane Neutral Spirit with Natural Flavors”
- “35% Alc./Vol.”
- “750 ml”
- “Bottled by QM Spirits, LLC” and “Nashville, TN” - “Government Warning: (1) According to the Surgeon General, women should not drink alcoholic beverages during
pregnancy because of the risk of birth defects. (2) Consumption of alcoholic beverages impairs your ability to
drive a car or operate machinery, and may cause health problems.” (text in previous quotes must be in all
capitalized letters, text must be 2 MM in height and quote must be separated 2MM by all other text)
- Must be dedicated empty space for bar code (approximately 0.75in. height x 1.25in. length)
Updates

Target Market(s)

Label should have mass market appeal.
Age: 21 – 28 years old (primary target market is 21+ year old college students and recent graduates)
Target Market Gender: Both male and female, with emphasis on male
Consumption Focus: Spirit will be consumed typically as a shot, primarily at bars and secondarily off premise (label design will be critical for making our product highly visible behind a bar)
Marketing Theme: South American elements. The official Luna de Cobre mascot is a llama and the incorporation and use of a llama somewhere (however large or small) on the bottle is encourage but by no means required.

Industry/Entity Type

Health

Requirements
Should not have
• Elements that may lead a potential consumer to believe the beverage is a craft liquor or an artisan brand. Please do not include images of peppers.

```html
<!DOCTYPE html>
<html lang="en">
<head>
<meta charset="utf-8">
<title>Luna de Cobre – Aguardiente Label</title>
<link rel="stylesheet" href="https://fonts.googleapis.com/css2?family=Marcellus&family=Pinyon+Script&family=Crimson+Text:ital,wght@0,400;0,600;1,600&display=swap">
<style>
  :root {
    --page: #ffffff;
    --label-red: #8e1d18;
    --label-red-deep: #5c0f0c;
    --medallion-top: #c4532c;
    --medallion-bottom: #6a1a12;
    --copper-light: #f0b28c;
    --copper-mid: #c47a55;
    --copper-dark: #7a3620;
    --ribbon: #7c3a22;
    --ribbon-dark: #4e2112;
    --cream: #f3e6da;
    --tan: #bba597;
    --llama: #b39c8b;
  }
  html, body {
    margin: 0;
    padding: 0;
    width: 1200px;
    height: 1200px;
    overflow: hidden;
    background: var(--page);
  }
  .label-canvas {
    display: block;
    width: 1200px;
    height: 1200px;
  }
  .brand-name {
    font-family: "Marcellus", serif;
    fill: var(--cream);
    font-size: 54px;
    letter-spacing: 1px;
  }
  .brand-name .connector { font-size: 36px; }
  .since-mark {
    font-family: "Marcellus", serif;
    fill: var(--tan);
    font-size: 22px;
    letter-spacing: 2px;
  }
  .category {
    font-family: "Pinyon Script", cursive;
    fill: var(--tan);
    font-size: 46px;
  }
  .descriptor {
    font-family: "Crimson Text", serif;
    font-style: italic;
    font-weight: 600;
    fill: var(--cream);
    font-size: 27px;
  }
  .strength {
    font-family: "Crimson Text", serif;
    fill: var(--cream);
    font-size: 23px;
  }
  .volume {
    font-family: "Crimson Text", serif;
    fill: var(--cream);
    font-size: 38px;
  }
</style>
</head>
<body>
<svg class="label-canvas" viewBox="0 0 1200 1200" xmlns="http://www.w3.org/2000/svg">
  <defs>
    <linearGradient id="copperRing" x1="0" y1="0" x2="1" y2="1">
      <stop offset="0" stop-color="var(--copper-light)"/>
      <stop offset="0.45" stop-color="var(--copper-mid)"/>
      <stop offset="0.7" stop-color="var(--copper-dark)"/>
      <stop offset="1" stop-color="var(--copper-light)"/>
    </linearGradient>
    <radialGradient id="labelBody" cx="0.5" cy="0.45" r="0.6">
      <stop offset="0" stop-color="var(--label-red)"/>
      <stop offset="0.75" stop-color="#7a1713"/>
      <stop offset="1" stop-color="var(--label-red-deep)"/>
    </radialGradient>
    <linearGradient id="medallionFill" x1="0" y1="0" x2="0" y2="1">
      <stop offset="0" stop-color="var(--medallion-top)"/>
      <stop offset="0.55" stop-color="#8f2f1b"/>
      <stop offset="1" stop-color="var(--medallion-bottom)"/>
    </linearGradient>
    <linearGradient id="ribbonFill" x1="0" y1="0" x2="0" y2="1">
      <stop offset="0" stop-color="#9a4a2c"/>
      <stop offset="0.5" stop-color="var(--ribbon)"/>
      <stop offset="1" stop-color="var(--ribbon-dark)"/>
    </linearGradient>
  </defs>

  <!-- label body -->
  <g class="label">
    <ellipse class="label-border" cx="600" cy="600" rx="314" ry="524" fill="url(#copperRing)"/>
    <ellipse class="label-field" cx="600" cy="600" rx="302" ry="512" fill="url(#labelBody)"/>

    <!-- medallion -->
    <g class="medallion">
      <ellipse cx="600" cy="470" rx="256" ry="346" fill="url(#copperRing)"/>
      <ellipse cx="600" cy="470" rx="246" ry="336" fill="url(#medallionFill)"/>
      <ellipse cx="600" cy="470" rx="226" ry="316" fill="none" stroke="var(--copper-mid)" stroke-opacity="0.45" stroke-width="2"/>

      <rect class="mascot-area" x="520" y="232" width="170" height="236" rx="18"
            fill="var(--llama)" role="img" aria-label="Silhouette of a standing llama, the brand mascot"/>
      <path d="M430 470 Q600 455 770 470" stroke="var(--llama)" stroke-width="3" fill="none"/>

      <text class="since-mark" x="474" y="442" text-anchor="middle">SINCE</text>
      <text class="since-mark" x="724" y="442" text-anchor="middle">2013</text>

      <text class="category" x="600" y="662" text-anchor="middle">Aguardiente</text>
      <rect class="ornament-area" x="586" y="702" width="28" height="28"
            fill="var(--tan)" role="img" aria-label="Small four-point diamond ornament"/>
    </g>

    <!-- name ribbon -->
    <g class="name-ribbon">
      <path d="M240 512 L330 512 L330 600 L240 600 L270 556 Z" fill="var(--ribbon-dark)"/>
      <path d="M960 512 L870 512 L870 600 L960 600 L930 556 Z" fill="var(--ribbon-dark)"/>
      <rect x="292" y="490" width="616" height="96" fill="url(#ribbonFill)"/>
      <line x1="292" y1="497" x2="908" y2="497" stroke="var(--copper-light)" stroke-opacity="0.5" stroke-width="2"/>
      <line x1="292" y1="579" x2="908" y2="579" stroke="var(--copper-light)" stroke-opacity="0.35" stroke-width="2"/>
      <text class="brand-name" x="600" y="556" text-anchor="middle">LUNA <tspan class="connector">de</tspan> COBRE</text>
    </g>

    <!-- product details -->
    <text class="descriptor" x="600" y="868" text-anchor="middle">Cane Neutral Spirit with Natural Flavors</text>
    <text class="strength" x="600" y="938" text-anchor="middle">35% Alc./Vol.</text>
    <text class="volume" x="600" y="988" text-anchor="middle">750 ml</text>
  </g>
</svg>
</body>
</html>
```